Bellwick Group, Accounting Audit Advisory Flyer Design

We need a flyer designed for our company Bellwick Group SA we need the flyer to outline our services.
We are an accounting firm who specializes in taxation, accounting, auditing and business advisory. Our tag phrase is "giving business direction", our corporate color is a gradient blue with a white background and we also feature a compass rose.
We are looking for a clean, clear and crisp final design to reflect our vision for assisting successful businesses grow.

Target Market(s)

Small Medium businesses, high income earning individuals

Industry/Entity Type

Business Service

Font styles to use
Sans Serif

Colors
0393ce
34a6d7
85cae6
0555a3
edf7fb

Requirements
Must have
• Editable text boxes
• Logo
• Editable contact details on the back page
• Double sided with 2 folds

```html
<!DOCTYPE html>
<html lang="en">
<head>
<meta charset="utf-8">
<title>Bellwick Group – Flyer</title>
<link rel="stylesheet" href="https://fonts.googleapis.com/css2?family=Open+Sans:wght@400;600;700&family=Oswald:wght@400;600&display=swap">
<style>
  :root{
    --blue-deep:#0555a3;
    --blue-main:#0393ce;
    --blue-mid:#34a6d7;
    --blue-soft:#85cae6;
    --blue-pale:#edf7fb;
    --ink:#2a2f36;
    --white:#ffffff;
    --page-bg:#e9edf1;
  }
  *{box-sizing:border-box;margin:0;padding:0}
  html,body{width:900px;height:1200px;overflow:hidden;background:var(--page-bg);font-family:"Open Sans",Arial,sans-serif;color:var(--ink)}
  .canvas{position:relative;width:900px;height:1200px}
  .spread{position:absolute;left:40px;width:820px;height:560px;background:var(--white);overflow:hidden;box-shadow:0 4px 18px rgba(0,0,0,.18)}
  .spread--outside{top:30px}
  .spread--inside{top:610px}
  .panel{position:absolute;top:0;width:410px;height:560px;overflow:hidden}
  .panel--left{left:0}
  .panel--right{left:410px}
  .fold{position:absolute;left:409px;top:0;width:2px;height:560px;background:rgba(0,0,0,.06);z-index:5}
  .shapes{position:absolute;inset:0;width:100%;height:100%}
  .photo{position:absolute}
  .photo--office{left:0;top:0;width:410px;height:235px;background:linear-gradient(135deg,#1c2a3c 0%,#4a6f95 45%,#c9d8e6 100%);clip-path:polygon(0 0,100% 0,100% 78%,0 100%)}
  .photo--finance{left:0;top:0;width:410px;height:190px;background:linear-gradient(160deg,#dfe9f2 0%,#8fb2cf 55%,#3f6f99 100%);clip-path:polygon(0 0,100% 0,100% 100%,0 70%)}
  .photo--writing{left:0;top:0;width:410px;height:175px;background:linear-gradient(120deg,#e6ebf0 0%,#b9c6d3 50%,#6d8499 100%);clip-path:polygon(0 0,100% 0,100% 55%,0 100%)}
  .photo--charts{left:0;top:120px;width:190px;height:110px;background:linear-gradient(150deg,#f2f5f8 0%,#9fc4dc 60%,#5a8fb5 100%);clip-path:polygon(0 25%,100% 0,100% 70%,0 100%)}
  .photo--checklist{left:150px;top:330px;width:260px;height:230px;background:linear-gradient(145deg,#f3f5f7 0%,#cbd6e0 55%,#7d93a8 100%);clip-path:ellipse(100% 95% at 100% 100%)}
  .headline{position:absolute;left:150px;top:52px;font-family:"Oswald",Arial,sans-serif;font-weight:600;font-size:40px;letter-spacing:3px;color:#111}
  .label-bar{position:absolute;height:26px;padding:0 12px;background:var(--blue-deep);color:var(--white);font-weight:700;font-size:15px;line-height:26px}
  .contact-list{position:absolute;left:24px;top:300px;list-style:none}
  .contact-list li{display:flex;align-items:center;gap:10px;font-size:14px;margin-bottom:12px}
  .contact-icon{width:22px;height:22px;border-radius:50%;background:#5b6168;display:flex;align-items:center;justify-content:center}
  .social{position:absolute;right:16px;top:14px;display:flex;gap:6px}
  .social span{width:18px;height:18px;border-radius:50%;background:var(--blue-main)}
  .social span:nth-child(3){background:#c4463a}
  .brand{position:absolute;left:30px;top:232px;width:120px;height:120px;border-radius:50%;background:var(--white);box-shadow:0 2px 10px rgba(0,0,0,.25);display:flex;align-items:center;justify-content:center;text-align:center;font-weight:700;font-size:20px;line-height:1.15;color:var(--ink)}
  .tagline{position:absolute;right:26px;top:378px;text-align:center;font-family:"Oswald",Arial,sans-serif;font-size:26px;line-height:1.15;color:var(--blue-deep)}
  .body-copy{position:absolute;font-size:11.5px;line-height:1.45;color:var(--ink)}
</style>
</head>
<body>
<div class="canvas">

  <!-- Outside spread -->
  <section class="spread spread--outside">
    <div class="panel panel--left">
      <div class="photo photo--office" role="img" aria-label="Photo of a businessman in a suit working at a desk"></div>
      <h1 class="headline">TAXES</h1>
      <svg class="shapes" viewBox="0 0 410 560" aria-hidden="true">
        <defs>
          <linearGradient id="g1" x1="0" y1="0" x2="1" y2="0">
            <stop offset="0" stop-color="#0555a3"/><stop offset="1" stop-color="#34a6d7"/>
          </linearGradient>
        </defs>
        <path d="M0 235 L410 183 L410 200 L0 250Z" fill="url(#g1)"/>
        <path d="M0 440 C120 400 260 420 410 470 L410 560 L0 560Z" fill="#85cae6"/>
        <path d="M0 470 C140 430 280 460 410 500 L410 560 L0 560Z" fill="url(#g1)"/>
        <path d="M0 515 C150 485 290 505 410 540 L410 560 L0 560Z" fill="#0555a3"/>
      </svg>
      <div class="label-bar" style="left:24px;top:262px">Contact us:</div>
      <ul class="contact-list">
        <li><span class="contact-icon"><svg width="12" height="12" viewBox="0 0 24 24"><path fill="#fff" d="M6.6 10.8a15 15 0 006.6 6.6l2.2-2.2c.3-.3.7-.4 1-.2 1.1.4 2.3.6 3.6.6.6 0 1 .4 1 1V20c0 .6-.4 1-1 1A17 17 0 013 4c0-.6.4-1 1-1h3.5c.6 0 1 .4 1 1 0 1.3.2 2.5.6 3.6.1.3 0 .7-.2 1z"/></svg></span>0147-382-615</li>
        <li><span class="contact-icon"><svg width="12" height="12" viewBox="0 0 24 24"><circle cx="12" cy="12" r="9" fill="none" stroke="#fff" stroke-width="2"/><path d="M3 12h18M12 3c3 3 3 15 0 18M12 3c-3 3-3 15 0 18" fill="none" stroke="#fff" stroke-width="1.6"/></svg></span>www.bellwickgroup.com</li>
        <li><span class="contact-icon"><svg width="12" height="12" viewBox="0 0 24 24"><rect x="3" y="6" width="18" height="12" fill="none" stroke="#fff" stroke-width="2"/><path d="M3 6l9 7 9-7" fill="none" stroke="#fff" stroke-width="2"/></svg></span>hello@bellwickgroup.com</li>
      </ul>
    </div>

    <div class="panel panel--right">
      <div class="photo photo--finance" role="img" aria-label="Photo of financial charts with a pen and calculator"></div>
      <div class="social" aria-hidden="true"><span></span><span></span><span></span></div>
      <svg class="shapes" viewBox="0 0 410 560" aria-hidden="true">
        <defs>
          <linearGradient id="g2" x1="0" y1="0" x2="1" y2="1">
            <stop offset="0" stop-color="#0555a3"/><stop offset="1" stop-color="#34a6d7"/>
          </linearGradient>
        </defs>
        <path d="M0 133 L410 190 L410 215 L0 150Z" fill="url(#g2)"/>
        <path d="M0 200 L190 165 L410 250 L410 330 L160 230 L0 290Z" fill="#edf7fb"/>
        <path d="M160 230 L410 330 L410 352 L150 245Z" fill="url(#g2)"/>
        <path d="M0 300 L150 245 L170 258 L0 330Z" fill="#85cae6"/>
        <path d="M0 470 C140 440 280 470 410 455 L410 560 L0 560Z" fill="#85cae6"/>
        <path d="M0 500 C150 470 290 500 410 480 L410 560 L0 560Z" fill="url(#g2)"/>
      </svg>
      <div class="brand">Bellwick<br>Group</div>
      <p class="tagline">giving<br>business direction</p>
    </div>
    <div class="fold"></div>
  </section>

  <!-- Inside spread -->
  <section class="spread spread--inside">
    <div class="panel panel--left">
      <div class="photo photo--writing" role="img" aria-label="Photo of hands writing on a document"></div>
      <div class="photo photo--charts" role="img" aria-label="Photo of printed financial charts"></div>
      <svg class="shapes" viewBox="0 0 410 560" aria-hidden="true">
        <defs>
          <linearGradient id="g3" x1="0" y1="0" x2="1" y2="0">
            <stop offset="0" stop-color="#0555a3"/><stop offset="1" stop-color="#34a6d7"/>
          </linearGradient>
        </defs>
        <path d="M190 130 L410 96 L410 116 L190 150Z" fill="url(#g3)"/>
        <path d="M0 232 L410 150 L410 165 L0 245Z" fill="#85cae6"/>
      </svg>
      <div class="label-bar" style="left:20px;top:262px">About us:</div>
      <p class="body-copy" style="left:20px;top:296px;width:370px">Bellwick Group is an accounting firm serving small and medium businesses and high income individuals. We combine careful tax planning, clear reporting and practical advice so owners can focus on growth with confidence in their numbers.</p>
      <div class="label-bar" style="left:20px;top:380px">Service:</div>
      <p class="body-copy" style="left:20px;top:414px;width:370px">Taxation, accounting, auditing and business advisory delivered by one experienced team, with timely filings and honest guidance every step of the way.</p>
    </div>

    <div class="panel panel--right">
      <svg class="shapes" viewBox="0 0 410 560" aria-hidden="true">
        <defs>
          <linearGradient id="g4" x1="0" y1="0" x2="1" y2="1">
            <stop offset="0" stop-color="#0555a3"/><stop offset="1" stop-color="#34a6d7"/>
          </linearGradient>
        </defs>
        <path d="M0 0 L150 0 L0 120Z" fill="url(#g4)"/>
        <path d="M170 0 L260 0 L0 200 L0 150Z" fill="#85cae6"/>
        <path d="M280 0 L300 0 L0 230 L0 214Z" fill="#0393ce"/>
        <path d="M0 560 L0 470 C80 500 130 540 150 560Z" fill="#edf7fb"/>
      </svg>
      <div class="label-bar" style="left:150px;top:112px">Our Information:</div>
      <p class="body-copy" style="left:150px;top:146px;width:240px">Our advisors meet with you to understand your goals, review your records and build a plan that fits your business. From monthly bookkeeping to annual audits, we keep every report accurate and on time. Clients receive direct access to a partner, clear fees and regular reviews that turn figures into decisions.</p>
      <div class="photo photo--checklist" role="img" aria-label="Photo of a hand ticking an audit checklist with a pen"></div>
    </div>
    <div class="fold"></div>
  </section>

</div>
</body>
</html>
```